Graphic background for 10 Pull Up Banners

To produce a graphic background for a 100 cm wide by 200 cm high Pull-Up Display banner containing a Buddhist text in three languages: Tibetan, Mandarin and English. Please refer to uploaded file "Elements of Pull Up Banner". The design should be simple (not drawing attention away from the text). This design should then be varied for or extended to the next banner and so on until the 10th banner. When the banners are lined up, they should form a single design that is 1000 cm wide by 200 cm high.
An alternative way to look at the project is to produce a graphic background of 1000 cm width by 200 cm height that is then splitted into ten separate 100 cm wide by 200 cm high graphic to be used as background for 10 Buddhist texts (text 1, 2, 3, 4, 5, 6, 7, 8, 9a, 9b) on 10 Pull-Up Display Banners, the text in each banner being in the three languages mentioned earlier.
In either perspective, the design should be simple and not draw attention away from the texts. See uploaded PDF file "Examples.pdf"
For attendees at a Buddhist Event.

```html
<!DOCTYPE html>
<html lang="en">
<head>
<meta charset="utf-8">
<title>Pull-Up Banners – Buddhist Texts</title>
<link rel="stylesheet" href="https://fonts.googleapis.com/css2?family=Noto+Sans+SC:wght@400;500&family=Noto+Serif+Tibetan:wght@400&family=Open+Sans:wght@400;600&display=swap">
<style>
  :root{
    --banner-red:#e3262f;
    --banner-red-deep:#d81f2a;
    --gold:#d6ab52;
    --gold-light:#f0d48c;
    --ink-white:#ffffff;
    --page:#ffffff;
  }
  *{margin:0;padding:0;box-sizing:border-box}
  html,body{width:1200px;height:778px;overflow:hidden;background:var(--page)}
  .banner-row{position:relative;width:1200px;height:778px}
  .banner{
    position:absolute;top:0;width:390px;height:778px;overflow:hidden;
    background:radial-gradient(circle at 50% 40%,var(--banner-red) 0%,var(--banner-red-deep) 100%);
    color:var(--ink-white);text-align:center;
  }
  .banner--one{left:0}
  .banner--two{left:406px}
  .banner--three{left:810px}

  .knot-band{position:absolute;left:0;width:100%;height:40px;
    background:linear-gradient(180deg,var(--gold-light),var(--gold) 50%,var(--gold-light));opacity:.85}
  .knot-band--top{top:16px}
  .knot-band--bottom{top:724px}

  .medallion{position:absolute;left:157px;top:6px;width:76px;height:76px;border-radius:50%;
    background:radial-gradient(circle,#f6ece6 0%,#e9cfc8 70%,#fff 100%);
    border:3px solid var(--gold);}

  .title{position:absolute;left:0;width:100%;font-family:"Noto Sans SC","Open Sans",sans-serif;font-weight:400}
  .title .en{font-family:"Open Sans",sans-serif}
  .title--main{top:82px;font-size:16px}
  .title--main .en{font-weight:600;font-size:16px;margin-left:10px}
  .title--main .dash{margin:0 14px}
  .title--sub{top:84px;font-size:12.5px}
  .title--sub .dash{margin:0 6px}

  .divider{position:absolute;left:75px;width:240px;height:10px}
  .divider::before{content:"";position:absolute;left:0;right:0;top:4.5px;border-top:1px solid var(--ink-white)}
  .divider::after{content:"";position:absolute;left:50%;top:0;width:10px;height:10px;margin-left:-5px;
    border-radius:50%;background:var(--banner-red);border:1px solid var(--ink-white)}

  .verse{position:absolute;left:0;width:100%}
  .verse p{white-space:nowrap}

  .tibetan{font-family:"Noto Serif Tibetan",serif}
  .chinese{font-family:"Noto Sans SC",sans-serif}
  .english{font-family:"Open Sans",sans-serif}

  /* banner one */
  .list-tibetan{top:120px;font-size:9px;line-height:15.6px}
  .list-chinese{top:316px;font-size:9px;line-height:14.8px}
  .footnotes{position:absolute;left:0;width:100%;top:488px;font-family:"Noto Sans SC",sans-serif;font-size:6px;line-height:14px}
  .list-english{top:550px;font-size:7px;line-height:14.2px;font-weight:400}

  /* banners two and three */
  .verse-tibetan{top:136px;font-size:18px;line-height:26.5px}
  .verse-chinese{top:296px;font-size:16px;line-height:22.4px;letter-spacing:.5px}
  .verse-english{top:455px;font-size:11px;line-height:29.6px;font-weight:600}
</style>
</head>
<body>
<main class="banner-row">

  <section class="banner banner--one">
    <div class="knot-band knot-band--top" role="img" aria-label="Gold endless-knot ornament band"></div>
    <div class="medallion" role="img" aria-label="Circular medallion with a seated Buddhist deity illustration"></div>
    <h1 class="title title--main">十个误解<span class="dash">-</span><span class="en">Ten Mistaking</span></h1>
    <div class="divider" style="top:109px"></div>
    <div class="verse list-tibetan tibetan" lang="bo">
      <p>དད་པ་དང་འདོད་པ་ནོར་ས་ཡོད།།</p>
      <p>བྱམས་སྙིང་རྗེ་དང་ཆགས་པ་ནོར་ས་ཡོད།།</p>
      <p>ཤེས་བྱ་གཤིས་ཀྱི་སྟོང་པ་དང་བློས་བྱས་ཀྱི་སྟོང་པ་ནོར་ས་ཡོད།།</p>
      <p>ཆོས་ཀྱི་དབྱིངས་དང་ཆད་ལྟ་ནོར་ས་ཡོད།།</p>
      <p>ཉམས་སྦྱོང་དང་རྟོགས་པ་ནོར་ས་ཡོད།།</p>
      <p>བཙུན་པ་དང་ཆོས་འཚོལ་ནོར་ས་ཡོད།།</p>
      <p>འཁྲུལ་ཞིག་དང་བདུད་ཁྱེར་ནོར་ས་ཡོད།།</p>
      <p>གྲུབ་ཐོབ་དང་གཡོ་སྒྱུ་ནོར་ས་ཡོད།།</p>
      <p>གཞན་དོན་བྱེད་པ་དང་རང་དོན་བྱེད་པ་ནོར་ས་ཡོད།།</p>
      <p>ཐབས་མཁས་པ་དང་གཡོ་སྒྱུ་ནོར་ས་ཡོད།།</p>
    </div>
    <div class="divider" style="top:295px"></div>
    <div class="verse list-chinese chinese" lang="zh">
      <p>信心与爱欲可能混淆，</p>
      <p>慈悲与贪执可能混淆，</p>
      <p>所知¹本空与思维造作空性可能混淆，</p>
      <p>法界与断见²可能混淆，</p>
      <p>觉受与证悟可能混淆，</p>
      <p>尊者与神棍可能混淆，</p>
      <p>破惑与著魔可能混淆，</p>
      <p>成就者与骗子可能混淆，</p>
      <p>利他与自利可能混淆，</p>
      <p>方便善巧与谄媚哄骗可能混淆。</p>
    </div>
    <div class="footnotes" lang="zh">
      <p>1．所知：可以认识的外境。</p>
      <p>2．断见：否定因果、前生、后世等说法的见解。</p>
    </div>
    <div class="divider" style="top:527px"></div>
    <div class="verse list-english english">
      <p>Desire can be mistaken for faith or devotion.</p>
      <p>Attachment can be mistaken for love and compassion.</p>
      <p>Conceptual emptiness can be mistaken for the emptiness of the nature of phenomena.</p>
      <p>Nihilism can be mistaken for the dharmadhatu.</p>
      <p>A meditative experience can be mistaken for realization.</p>
      <p>Outer religious practices can be mistaken for inner development of good qualities.</p>
      <p>A person in the grip of a demon can be mistaken for a person who has destroyed his own delusions.</p>
      <p>A charlatan can be mistaken for a siddha.</p>
      <p>An act to benefit yourself can be mistaken for an act to benefit others.</p>
      <p>Deviousness can be mistaken for skilful means.</p>
    </div>
    <div class="knot-band knot-band--bottom" role="img" aria-label="Gold endless-knot ornament band"></div>
  </section>

  <section class="banner banner--two">
    <div class="knot-band knot-band--top" role="img" aria-label="Gold endless-knot ornament band"></div>
    <div class="medallion" role="img" aria-label="Circular medallion with a seated Buddhist deity illustration"></div>
    <h2 class="title title--sub">欲与爱<span class="dash">-</span><span class="en">Desire &amp; Attachment</span></h2>
    <div class="divider" style="top:115px"></div>
    <div class="verse verse-tibetan tibetan" lang="bo">
      <p>འདོད་པ་མེད་ན་རང་དོན་མི་འགྲུབ་ཀྱང་།།</p>
      <p>འདོད་པ་ཡོད་ཚད་ཆགས་པ་མི་ཡིན་པས།།</p>
      <p>འདོད་དང་ཆགས་པའི་ཁྱད་པར་མ་ཤེས་པར།།</p>
      <p>འདོད་ཆགས་ལམ་དུ་ཁྱེར་ཞེས་སྨྲ་བ་ཧམ།།</p>
    </div>
    <div class="divider" style="top:261px"></div>
    <div class="verse verse-chinese chinese" lang="zh">
      <p>若无意欲则不成自利，</p>
      <p>然有意欲非为执着故，</p>
      <p>不知意欲执着差别即，</p>
      <p>贪执说所当取确荒唐。</p>
    </div>
    <div class="divider" style="top:419px"></div>
    <div class="verse verse-english english">
      <p>If you have no desire, your goal cannot be achieved.</p>
      <p>Since not all desire is attachment,</p>
      <p>not knowing how to differentiate desire from attachment,</p>
      <p>to talk about bringing passion into the path is absurd.</p>
    </div>
    <div class="knot-band knot-band--bottom" role="img" aria-label="Gold endless-knot ornament band"></div>
  </section>

  <section class="banner banner--three">
    <div class="knot-band knot-band--top" role="img" aria-label="Gold endless-knot ornament band"></div>
    <div class="medallion" role="img" aria-label="Circular medallion with a seated Buddhist deity illustration"></div>
    <h2 class="title title--sub">欲与爱<span class="dash">-</span><span class="en">Desire &amp; Attachment</span></h2>
    <div class="divider" style="top:115px"></div>
    <div class="verse verse-tibetan tibetan" lang="bo">
      <p>འདོད་པ་མེད་ན་རང་དོན་མི་འགྲུབ་ཀྱང་།།</p>
      <p>འདོད་པ་ཡོད་ཚད་ཆགས་པ་མི་ཡིན་པས།།</p>
      <p>འདོད་དང་ཆགས་པའི་ཁྱད་པར་མ་ཤེས་པར།།</p>
      <p>འདོད་ཆགས་ལམ་དུ་ཁྱེར་ཞེས་སྨྲ་བ་ཧམ།།</p>
    </div>
    <div class="divider" style="top:261px"></div>
    <div class="verse verse-chinese chinese" lang="zh">
      <p>若无意欲则不成自利，</p>
      <p>然有意欲非为执着故，</p>
      <p>不知意欲执着差别即，</p>
      <p>贪执说所当取确荒唐。</p>
    </div>
    <div class="divider" style="top:419px"></div>
    <div class="verse verse-english english">
      <p>If you have no desire, your goal cannot be achieved.</p>
      <p>Since not all desire is attachment,</p>
      <p>not knowing how to differentiate desire from attachment,</p>
      <p>to talk about bringing passion into the path is absurd.</p>
    </div>
    <div class="knot-band knot-band--bottom" role="img" aria-label="Gold endless-knot ornament band"></div>
  </section>

</main>
</body>
</html>
```